Tarvil GmbH business card

We Tarvil GmbH based in Switzerland are looking for a business card design. The Fresh Jung, appealing to customers of all kinds. We already have a logo to upload but still a business card. Details: Tarvil GmbH Address: Lindenweg 14b in 9412 Rudolfen. Tel: 41 76 392 00 47, web: Tarvil.ch, E-mail: info@Tarvil.ch Facebook: Tarvil GmbH. I am the Managing Director: Lukas Verholt. On reverse: Title: Transporter and bus rental Gross: Without deposit Super prices
Contact Information for Business Card
Siehe Projektbeschreibung
Requirements
Should not have
- Other pictures

```html
<!DOCTYPE html>
<html lang="de">
<head>
<meta charset="utf-8">
<title>Tarvil GmbH – Visitenkarte</title>
<link rel="stylesheet" href="https://fonts.googleapis.com/css2?family=Roboto:wght@400;500;700&display=swap">
<style>
  :root {
    --backdrop: #e8e8e8;
    --paper: #f4f4f4;
    --navy: #1e1f63;
    --steel: #7b9cc0;
    --ink: #333338;
    --icon: #6f7f99;
    --on-navy: #f2f3f8;
  }
  * { margin: 0; padding: 0; box-sizing: border-box; }
  html, body {
    width: 1200px; height: 576px; overflow: hidden;
    background: var(--backdrop);
    font-family: "Roboto", Arial, sans-serif;
  }
  .canvas { position: relative; width: 1200px; height: 576px; }

  .card { position: absolute; top: 138px; width: 485px; height: 294px; border-radius: 7px; }
  .card--front { left: 81px; background: var(--paper); }
  .card--back { left: 602px; background: var(--navy); }

  .accent-bar { position: absolute; left: 0; top: 29px; width: 13px; height: 47px; background: var(--steel); }
  .person { position: absolute; left: 32px; top: 38px; }
  .person__name { font-size: 18px; font-weight: 700; color: var(--navy); line-height: 1.1; }
  .person__role { font-size: 11px; color: var(--ink); margin-top: 5px; }

  .brand {
    position: absolute; right: 26px; top: 100px;
    display: flex; align-items: center; gap: 8px;
  }
  .brand__mark { width: 16px; height: 16px; background: var(--steel); }
  .brand__name { font-size: 34px; font-weight: 700; color: var(--navy); letter-spacing: 0.5px; }

  .contact { position: absolute; left: 32px; top: 182px; list-style: none; }
  .contact__item {
    display: flex; align-items: center; gap: 10px;
    font-size: 12px; color: var(--ink); height: 16.5px;
  }
  .contact__icon { width: 11px; height: 11px; flex: none; }
  .address { position: absolute; left: 32px; top: 217px; font-size: 12px; color: var(--ink); }
  .contact + .address { top: 255px; }

  .offer {
    position: absolute; left: 0; right: 0; top: 98px;
    text-align: center; color: var(--on-navy);
  }
  .offer__title { font-size: 17px; }
  .offer__headline { font-size: 25px; font-weight: 700; color: var(--steel); margin-top: 6px; letter-spacing: 0.3px; }
  .offer__tagline { font-size: 16px; margin-top: 3px; }
</style>
</head>
<body>
<main class="canvas">
  <section class="card card--front">
    <div class="accent-bar"></div>
    <div class="person">
      <p class="person__name">Lukas Verholt</p>
      <p class="person__role">Geschäftsführer</p>
    </div>
    <div class="brand">
      <span class="brand__mark"></span>
      <span class="brand__name">Tarvil</span>
    </div>
    <ul class="contact">
      <li class="contact__item">
        <svg class="contact__icon" viewBox="0 0 12 12"><path fill="var(--icon)" d="M1 4c0-1.5 2-2.5 5-2.5S11 2.5 11 4v1H8.5V3.8h-5V5H1zM3 6h6l1.5 4.5h-9z"/></svg>
        +41 76 392 00 47
      </li>
      <li class="contact__item">
        <svg class="contact__icon" viewBox="0 0 12 12"><g fill="none" stroke="var(--icon)" stroke-width="1"><circle cx="6" cy="6" r="5"/><ellipse cx="6" cy="6" rx="2.2" ry="5"/><path d="M1 6h10M2 3.5h8M2 8.5h8"/></g></svg>
        www.Tarvil.ch
      </li>
      <li class="contact__item">
        <svg class="contact__icon" viewBox="0 0 12 12"><rect x="0.5" y="2.5" width="11" height="7.5" fill="var(--icon)"/><path d="M0.5 2.5l5.5 4.5 5.5-4.5" fill="none" stroke="var(--paper)" stroke-width="0.9"/></svg>
        info@Tarvil.ch
      </li>
      <li class="contact__item">
        <svg class="contact__icon" viewBox="0 0 12 12"><rect x="0.5" y="0.5" width="11" height="11" rx="1.5" fill="var(--icon)"/></svg>
        Tarvil GmbH
      </li>
    </ul>
    <p class="address">Lindenweg 14b in 9412 Rudolfen</p>
  </section>

  <section class="card card--back">
    <div class="offer">
      <p class="offer__title">Transporter und Bus Vermietung</p>
      <p class="offer__headline">OHNE KAUTION</p>
      <p class="offer__tagline">Super Preise</p>
    </div>
  </section>
</main>
</body>
</html>
```